Construction Company informative web page

Torvell Builders is a new company that combine Project Manager and kitchen & bath design with Interior remodeling for houses or business (commercial and residential construction)
We want to show our reviews, portafolio and background experience
Updates

Reason: I would like to have the time to interact with the favorite designers to fine tune the website also I'd like to see more designs

Hello Everybody,

Thank you for your time, please make the corrections shown below:

Pages:

1. Home:

1.  Includes a welcome and a briefly background:

2. Right side vertically show a few reviews with the option read more to open it, just the Name and last name, city and review (no start ratings)

3. Facebook and youtube link

4. Left side below shows 4 slides show with pictures and titles:

1. Kitchen Design

2. Bath Design

3. General Remodeling

4. Commercial Projects

2. About Us:

Our Professionals:

Torvell Builders Project Manager  is responsible to set the project schedule, request materials  and coordinate the delivery on time.  The Project Manager focus is ensuring  the best customer satisfaction in every step of the project until the final product is completed.

The Designer gives you the best ideas in 3D format,   getting the best lay out possible.  understanding your needs, defining your unique style putting together all your requirements and ideas to make the best match for you, making sure you get the best products within your budget

Torvell Builders have a high quality group of trade specialist; plumbers, electricians and installers. Our crew is pleasant to work with,  safety and cleaning values  and very detailed oriented

Our Core Values

As our slogan your project is our business, well we really mean it our job is not just to do the job is to guaranteed a pleasant experience with great costumer service, communication, quality, in time and within your budget

 

1. Services:

1. Commercial

2. Residential

2. Portafolio:  Separated pictures in each project, I want to have a brief description in each picture

1. Kitchen Design

2. Bath Design

3. General Remodeling

4. Commercial Projects

 

1. Contact Us:  

1. Project Management Department:

Contact Person: Rhonda Kestling

Email: rhonda@torvellbuilders.com

2. Office Management Department:

Contact Person: Lou Brambery

Email: info@torvellbuilders.com

 

Please try to pick design style shown in business card to match a little bit. Keep the color tones

I want the logo in the upper left corner and a very nice picture with a kitchen (warm colors)mostly American northeast style like the main pic of the web.

I want the web page is able to be fully open in computers, tablets and cellphones

Please send me an email to torvellbuilders1@mailnest.com so I can send you my logo and any other information to be incorporated

Thank you

Hello Everybody,

Thank you for your time, please make the corrections accordingly:

Pages:

1. Home: Includes a welcome and a briefly say something about our background 

Hello, I just upload my logo and my business card so you can adjust your designs

Please presented responsive format

I want coding the webpage too

Please read carefully my last update

Thank you so much!                                   

Industry/Entity Type

Residential

Requirements
Nice to have
• Should it has a Newsletter subscription with the email at the bottom of the home page
In contact page: A box "Contact us for a free estimate"

```html
<!DOCTYPE html>
<html lang="en">
<head>
<meta charset="utf-8">
<title>Torvell Builders – Home</title>
<link href="https://fonts.googleapis.com/css2?family=Lato:wght@300;400;700&display=swap" rel="stylesheet">
<style>
:root{
  --maroon:#7a1f1c;
  --maroon-deep:#6b1a17;
  --ink:#333;
  --grey:#8a8f93;
  --light-grey:#b5b9bc;
  --line:#e4e6e8;
  --card:#eef1f4;
  --slate:#2f363a;
  --footer:#363d41;
  --footer-bar:#2c3236;
  --footer-text:#aab0b4;
  --cream:#ede8dc;
}
*{margin:0;padding:0;box-sizing:border-box}
html,body{width:876px;height:1200px;overflow:hidden;background:#fff}
body{font-family:'Lato',sans-serif;color:var(--ink);position:relative}
.abs{position:absolute}

/* header */
.topline{left:0;top:27px;width:876px;height:1px;background:var(--line)}
.logo{left:106px;top:0;width:93px;height:84px;background:var(--maroon);color:#f3e9dc;text-align:center;padding-top:26px}
.logo .name{font-size:12px;font-weight:700;line-height:14px}
.logo .tag{font-size:6.5px;margin-top:8px;font-weight:400}
.top-contacts{right:104px;top:7px;display:flex;align-items:center;gap:18px;white-space:nowrap}
.top-contact{font-size:7.5px;color:var(--light-grey);display:flex;align-items:center;gap:6px}
.top-contact svg{flex:none}
.nav{top:52px;font-size:9.5px}
.nav a{position:absolute;white-space:nowrap;color:#555;text-decoration:none}
.nav a.nav-current{color:var(--maroon)}

/* hero */
.hero{left:0;top:89px;width:876px;height:328px;background:linear-gradient(100deg,#e9eef0 0%,#f4f2ee 30%,#d9d3cb 60%,#c9c3bc 100%)}
.hero-caption{left:450px;top:179px;width:426px;height:124px;background:rgba(110,25,22,.92);color:#fff;padding:27px 28px}
.hero-caption h1{font-weight:300;font-size:20px;margin-bottom:12px}
.hero-caption p{font-size:8.5px;line-height:14px}
.dots{left:725px;top:396px;display:flex;gap:6px;align-items:center}
.dots span{width:6px;height:6px;border-radius:50%;background:#fff}
.dots span.on{width:9px;height:9px;background:var(--maroon);border:2px solid #fff}

/* portfolio */
.section-title{font-weight:300;font-size:21px;color:#444}
.portfolio-title{left:0;width:876px;top:433px;text-align:center}
.card{top:477px;width:209px;height:198px;background:var(--card);text-align:center}
.card .photo{width:209px;height:137px}
.card .t{font-size:10px;margin-top:15px;color:#333}
.card .s{font-size:8.5px;margin-top:6px;color:#999}
.card.active{background:var(--slate)}
.card.active .t{color:#fff}
.card.active .s{color:#c9cdd0}
.arrow{top:546px;width:41px;height:41px;border-radius:50%;background:var(--cream);display:flex;align-items:center;justify-content:center}

/* welcome */
.welcome-title{left:107px;top:715px}
.welcome-copy{left:104px;top:752px;width:330px;font-size:8.5px;line-height:14px;color:var(--grey)}
.checks{font-size:8.5px;color:var(--grey)}
.checks li{list-style:none;display:flex;align-items:center;gap:6px;height:20.5px}

/* reviews */
.review{left:450px;width:326px}
.review .avatar{position:absolute;left:0;top:0;width:55px;height:55px;border-radius:50%;background:radial-gradient(circle at 50% 40%,#d8c2ae,#6d6560)}
.review .body{position:absolute;left:68px;top:0;width:256px}
.review .nm{font-size:10px;color:#333}
.review .dt{font-size:8.5px;color:var(--grey);margin-top:2px;padding-bottom:4px;border-bottom:1px solid var(--line)}
.review .tx{font-size:8.5px;line-height:13.5px;color:var(--grey);margin-top:6px}

/* footer */
.footer{left:0;top:931px;width:876px;height:234px;background:var(--footer)}
.footer-bar{left:0;top:1165px;width:876px;height:35px;background:var(--footer-bar)}
.f-logo{left:136px;top:969px;width:74px;height:67px;background:var(--maroon);color:#f3e9dc;text-align:center;padding-top:20px}
.f-logo .name{font-size:10px;font-weight:700;line-height:12px}
.f-logo .tag{font-size:5.5px;margin-top:6px}
.f-about{left:104px;top:1043px;width:150px;font-size:8.5px;line-height:14px;color:var(--footer-text)}
.f-about p{margin-bottom:7px}
.f-about a{color:var(--footer-text);font-size:7.5px;text-decoration:underline}
.f-head{font-size:10px;font-weight:700;color:#fff}
.post{left:276px;width:150px;height:40px}
.post .th{position:absolute;left:0;top:0;width:37px;height:37px;background:linear-gradient(135deg,#8b949b,#cfd4d7)}
.post .pt{position:absolute;left:47px;top:0;font-size:8.5px;line-height:14px;color:var(--footer-text);white-space:nowrap}
.post .pd{position:absolute;left:47px;top:28px;font-size:7.5px;color:#7c848a}
.social{top:991px;left:450px;display:flex;gap:11px}
.social span{width:22px;height:22px;border-radius:50%;background:#5c6469}
.nl-copy{left:450px;top:1074px;width:160px;font-size:8.5px;line-height:15px;color:var(--footer-text)}
.nl-input{left:450px;top:1116px;width:112px;height:25px;background:#262b2e;color:#b9bec1;font-size:8.5px;padding:8px 8px}
.nl-btn{left:562px;top:1116px;width:59px;height:25px;background:var(--maroon);color:#fff;font-size:9px;text-align:center;padding-top:7px}
.cd{left:636px;font-size:8.5px;line-height:14px;color:var(--footer-text);display:flex;gap:9px;white-space:nowrap}
.cd svg{flex:none;margin-top:2px}
.map{left:638px;top:1089px;width:134px;height:54px;background:linear-gradient(135deg,#eae6dc,#f6f3ea 50%,#e5dfce);border:2px solid #fff}
.copy{left:104px;top:1177px;font-size:8.5px;color:var(--footer-text)}
.f-nav{top:1177px;font-size:8.5px}
.f-nav a{position:absolute;white-space:nowrap;color:var(--footer-text);text-decoration:none}
.f-nav a.nav-current{color:#fff}
</style>
</head>
<body>

<header>
  <div class="abs topline"></div>
  <div class="abs logo"><div class="name">Torvell<br>Builders</div><div class="tag">Your project is our business</div></div>
  <div class="abs top-contacts">
    <div class="top-contact">
      <svg width="20" height="12" viewBox="0 0 20 12"><g fill="none" stroke="#7a1f1c" stroke-width="1.2"><rect x="7" y="1" width="12" height="9"/><path d="M7 1l6 5 6-5"/><path d="M0 3h5M2 6h4M1 9h5"/></g></svg>
      <span>hello@torvellbuilders.com</span>
    </div>
    <div class="top-contact">
      <svg width="12" height="12" viewBox="0 0 12 12"><path d="M3 1l2 3-1 1c1 2 2 3 4 4l1-1 3 2-1 2C6 12 0 6 1 2z" fill="none" stroke="#7a1f1c" stroke-width="1.2"/></svg>
      <span>+1800.555.0147</span>
    </div>
  </div>
  <nav class="abs nav" style="left:0">
    <a class="nav-current" href="#" style="left:506px">Home</a>
    <a href="#" style="left:563px">Services</a>
    <a href="#" style="left:630px">Blog</a>
    <a href="#" style="left:680px">About</a>
    <a href="#" style="left:737px">Contact</a>
  </nav>
</header>

<section>
  <div class="abs hero" role="img" aria-label="Bright white bathroom interior with sink, plant and large windows"></div>
  <div class="abs hero-caption">
    <h1>Your Project is Our Business.</h1>
    <p>Maecenas bibendum lacus gravida placerat consequat. Vivamus quis hendrerit mauris. Vestibulum laoreet felis sed consectetur sollicitudin.</p>
  </div>
  <div class="abs dots"><span></span><span class="on"></span><span></span><span></span></div>
</section>

<section>
  <h2 class="abs section-title portfolio-title">Portfolio</h2>
  <div class="abs arrow" style="left:42px"><svg width="8" height="10" viewBox="0 0 8 10"><path d="M6 1L2 5l4 4" fill="none" stroke="#7a1f1c" stroke-width="1.4"/></svg></div>
  <div class="abs arrow" style="left:794px"><svg width="8" height="10" viewBox="0 0 8 10"><path d="M2 1l4 4-4 4" fill="none" stroke="#7a1f1c" stroke-width="1.4"/></svg></div>

  <div class="abs card" style="left:104px">
    <div class="photo" role="img" aria-label="White bathroom vanity with sink and potted plant" style="background:linear-gradient(135deg,#e8ecee,#cfd5d8 60%,#f2f2ef)"></div>
    <div class="t">Maecenas Bibendum</div><div class="s">Marketing Online</div>
  </div>
  <div class="abs card active" style="left:334px">
    <div class="photo" role="img" aria-label="Wooden dining table with a fruit bowl and red chairs" style="background:linear-gradient(180deg,#7a4a2e,#5e3520 55%,#6b5a22);position:relative">
      <svg style="position:absolute;left:81px;top:57px" width="48" height="20" viewBox="0 0 48 20"><rect width="20" height="20" fill="#fff"/><rect x="28" width="20" height="20" fill="#fff"/><path d="M7 13l6-6M7 10v3h3M10 7h3v3" stroke="#999" fill="none"/><path d="M38 6v8M34 10h8" stroke="#999" stroke-width="1.4"/></svg>
    </div>
    <div class="t">Maecenas Bibendum</div><div class="s">Marketing Online</div>
  </div>
  <div class="abs card" style="left:564px">
    <div class="photo" role="img" aria-label="Dining table with white chairs and an orange bowl" style="background:linear-gradient(180deg,#d9d6cf,#bfb7ab 55%,#8a6a4c)"></div>
    <div class="t">Maecenas Bibendum</div><div class="s">Marketing Online</div>
  </div>
</section>

<section>
  <h2 class="abs section-title welcome-title">Welcome to Torvell Builders</h2>
  <p class="abs welcome-copy">Maecenas bibendum lacus gravida placerat consequat. Vivamus quis hendrerit mauris. Vestibulum laoreet felis sed consectetur sollicitudin. Maecenas bibendum lacus gravida placerat consequat. Vivamus quis hendrerit mauris. Vestibulum laoreet felis sed consectetur sollicitudin.</p>
  <ul class="abs checks" style="left:104px;top:819px">
    <li><svg width="10" height="10" viewBox="0 0 10 10"><circle cx="5" cy="5" r="4.2" fill="none" stroke="#7a1f1c" stroke-width="1.3"/><path d="M3 5l1.5 1.5L7 3.8" fill="none" stroke="#7a1f1c" stroke-width="1.3"/></svg>Maecenas bibendum lacus gravida</li>
    <li><svg width="10" height="10" viewBox="0 0 10 10"><circle cx="5" cy="5" r="4.2" fill="none" stroke="#7a1f1c" stroke-width="1.3"/><path d="M3 5l1.5 1.5L7 3.8" fill="none" stroke="#7a1f1c" stroke-width="1.3"/></svg>Pacerat consequat.</li>
    <li><svg width="10" height="10" viewBox="0 0 10 10"><circle cx="5" cy="5" r="4.2" fill="none" stroke="#7a1f1c" stroke-width="1.3"/><path d="M3 5l1.5 1.5L7 3.8" fill="none" stroke="#7a1f1c" stroke-width="1.3"/></svg>Vivamus quis hendrerit mauris</li>
  </ul>
  <ul class="abs checks" style="left:277px;top:819px">
    <li><svg width="10" height="10" viewBox="0 0 10 10"><circle cx="5" cy="5" r="4.2" fill="none" stroke="#7a1f1c" stroke-width="1.3"/><path d="M3 5l1.5 1.5L7 3.8" fill="none" stroke="#7a1f1c" stroke-width="1.3"/></svg>Maecenas bibendum lacus gravida</li>
    <li><svg width="10" height="10" viewBox="0 0 10 10"><circle cx="5" cy="5" r="4.2" fill="none" stroke="#7a1f1c" stroke-width="1.3"/><path d="M3 5l1.5 1.5L7 3.8" fill="none" stroke="#7a1f1c" stroke-width="1.3"/></svg>Pacerat consequat.</li>
    <li><svg width="10" height="10" viewBox="0 0 10 10"><circle cx="5" cy="5" r="4.2" fill="none" stroke="#7a1f1c" stroke-width="1.3"/><path d="M3 5l1.5 1.5L7 3.8" fill="none" stroke="#7a1f1c" stroke-width="1.3"/></svg>Vivamus quis hendrerit mauris</li>
  </ul>

  <div class="abs review" style="top:721px">
    <div class="avatar" role="img" aria-label="Reviewer portrait"></div>
    <div class="body">
      <div class="nm">Dale Verrick</div><div class="dt">October 26, 2014</div>
      <p class="tx">Maecenas bibendum lacus gravida placerat consequat. Vivamus quis hendrerit mauris. Vestibulum laoreet felis sed consectetur sollicitudin.</p>
    </div>
  </div>
  <div class="abs review" style="top:817px">
    <div class="avatar" role="img" aria-label="Reviewer portrait"></div>
    <div class="body">
      <div class="nm">Dale Verrick</div><div class="dt">October 26, 2014</div>
      <p class="tx">Maecenas bibendum lacus gravida placerat consequat. Vivamus quis hendrerit mauris. Vestibulum laoreet felis sed consectetur sollicitudin.</p>
    </div>
  </div>
</section>

<footer>
  <div class="abs footer"></div>
  <div class="abs f-logo"><div class="name">Torvell<br>Builders</div><div class="tag">Your project is our business</div></div>
  <div class="abs f-about">
    <p>Fusce gravida tortor felis, ac dictum risus sagittis id.</p>
    <p>Donec volutpat, mi vel egestas eleif-end, dolor arcu iaculis nunc. Fusce</p>
    <a href="#">LEAR MORE</a>
  </div>

  <div class="abs f-head" style="left:276px;top:968px">Recent Post</div>
  <div class="abs post" style="top:997px"><div class="th" role="img" aria-label="Post thumbnail"></div><div class="pt">Fusce gravida tortor felis,<br>ac dictum risus sagittis</div><div class="pd">October 15, 2013</div></div>
  <div class="abs post" style="top:1048px"><div class="th" role="img" aria-label="Post thumbnail"></div><div class="pt" style="color:#fff">Fusce gravida tortor felis,<br>ac dictum risus sagittis</div><div class="pd">October 15, 2013</div></div>
  <div class="abs post" style="top:1099px"><div class="th" role="img" aria-label="Post thumbnail"></div><div class="pt">Fusce gravida tortor felis,<br>ac dictum risus sagittis</div><div class="pd">October 15, 2013</div></div>

  <div class="abs f-head" style="left:450px;top:968px">Get Social</div>
  <div class="abs social"><span></span><span></span><span></span><span></span></div>
  <div class="abs f-head" style="left:450px;top:1046px">Newsletter</div>
  <p class="abs nl-copy">Ipsum dolor sit amet, teft consecte tur adipiscing elit ut eunt.</p>
  <div class="abs nl-input">Email Address</div>
  <div class="abs nl-btn">Subscribe</div>

  <div class="abs f-head" style="left:636px;top:968px">Contact Details</div>
  <div class="abs cd" style="top:996px"><svg width="12" height="11" viewBox="0 0 12 12"><path d="M3 1l2 3-1 1c1 2 2 3 4 4l1-1 3 2-1 2C6 12 0 6 1 2z" fill="#8b9297"/></svg><span>+1800-555-0147</span></div>
  <div class="abs cd" style="top:1017px"><svg width="12" height="10" viewBox="0 0 12 10"><rect x=".6" y=".6" width="10.8" height="8.8" fill="none" stroke="#8b9297" stroke-width="1.2"/><path d="M.6 .6L6 5l5.4-4.4" fill="none" stroke="#8b9297" stroke-width="1.2"/></svg><span>info@torvellbuilders.com</span></div>
  <div class="abs cd" style="top:1038px"><svg width="12" height="13" viewBox="0 0 10 13"><path d="M5 0a4 4 0 014 4c0 3-4 9-4 9S1 7 1 4a4 4 0 014-4z" fill="#8b9297"/><circle cx="5" cy="4" r="1.5" fill="#363d41"/></svg><span>Your Address, Your Country<br>Your Zip Code</span></div>
  <div class="abs map" role="img" aria-label="Street map showing the office location"></div>

  <div class="abs footer-bar"></div>
  <div class="abs copy">Copyright © 2014 - Torvell Builders. All Rights reserved</div>
  <nav class="abs f-nav" style="left:0">
    <a class="nav-current" href="#" style="left:508px">Home</a>
    <a href="#" style="left:565px">Services</a>
    <a href="#" style="left:631px">Blog</a>
    <a href="#" style="left:681px">About</a>
    <a href="#" style="left:739px">Contact</a>
  </nav>
</footer>

</body>
</html>
```